Hardcore nerd needs to stand out in a sea of dull Defence business cards

Wombat Devices is a new Australian consulting engineering company that turns research and theory into practical systems. No evangelistic fluff, just mathematics and physics into electronic and optical circuits for consumer products, scientific research or Defence applications.

We already have a recognised logo (provided) which is often dark blue/black on a light background but we're open to other combinations. (Us engineers tend to have limited aesthetic imagination :)

Some of our recent products have included:
* Instrumentation for electrical testing,
* Radar jammers,
* GPS antenna design,
* Satellite tracking systems,
* High power lasers

We're open to both single and double-sided designs - happy to be convinced either way.

P.S. Another group is working on the web page, so - alas - our web site is currently of no use for images/ideas...

Target Market(s)

Engineering managers,
Scientists

Contact Information for Business Card

Dr Colin Marsh
R&D Engineer

colin@wombatdevicesco.com.au
0427 563 210

PO Box XXX (to be confirmed)
Banks ACT 2913
Australia

Font styles to use
Serif
Sans Serif

Colors

Designer to choose colors to be used in the design.

Requirements
Must have
• My contact details!
• I've had many (great) "bold and plain" designs submitted already, so feel free to be artistically creative :)
• Happy to take advice re fonts/colours/printability etc.
Nice to have
• I'm not sure if "lists" are more at home on a CV than a business card, but representative services include:
• Applied electromagnetics
• RF and high speed electronics
• Signal and image processing
• Electro-optical and laser systems
• Concept-to-prototype design services
• If you're considering double sided cards, then often measuring/alignment grids/rulers feature on the back of similar cards.
• e.g. https://www.lumoptix-example.com/newgrouppage9.cfm?objectgroup_id=4815
• https://www.lumoptix-example.com/newgrouppage9.cfm?objectgroup_ID=4817
• ..or even a "Smith chart" (google will return lots)
• Generic images to represent a capability might work - googling images associated with keyword for each of these areas might help:
• - "passive radar", "phased array", "fdtd", "vircator"
• RF and high speed electronic design
• - "smith chart", "microstrip circuits", "dimensioned drawing", "electronic schematic"
• - "dft", "iir filter"
• - "optical cavity". "laser energy level diagram"
• Background/watermarked images outlines/wireframes/schematics would probably look OK.
Should not have
• If a list of projects/services is provided, it is important not to make the client feel that this is "all" the company can do. Engineering design is a creative discipline (like graphics :)
• Please, no stock "military" snaps like planes, missiles, etc!

```html
<!DOCTYPE html>
<html lang="en">
<head>
<meta charset="utf-8">
<title>Wombat Devices – Business Card</title>
<link rel="stylesheet" href="https://fonts.googleapis.com/css2?family=Open+Sans:wght@400;700&display=swap">
<style>
  :root {
    --backdrop: #e2e2e2;
    --card-white: #ffffff;
    --navy: #2b2a7c;
    --navy-deep: #25286a;
    --navy-light: #34378a;
    --navy-dark: #1d2058;
    --grey-text: #6b6b6b;
    --rule: #5a58a6;
  }
  * { box-sizing: border-box; margin: 0; padding: 0; }
  html, body {
    width: 1200px; height: 801px; overflow: hidden;
    background: var(--backdrop);
    font-family: "Open Sans", Arial, sans-serif;
  }
  .stage {
    position: relative; width: 1200px; height: 801px;
    display: flex; align-items: center; justify-content: center; gap: 50px;
  }
  .card {
    width: 525px; height: 300px; position: relative; overflow: hidden;
    box-shadow: 0 6px 18px rgba(0,0,0,0.12);
  }
  .card-front { background: var(--card-white); display: flex; align-items: center; }
  .brand {
    width: 232px; display: flex; align-items: center; gap: 10px;
    padding-left: 30px;
  }
  .brand-dot {
    width: 48px; height: 48px; border-radius: 50%;
    background: var(--navy); flex: none;
  }
  .brand-name {
    color: var(--navy); font-weight: 700; font-size: 18px;
    line-height: 1.1; text-transform: uppercase; letter-spacing: 0.5px;
  }
  .divider {
    width: 1px; height: 104px; background: var(--rule); margin-right: 14px;
  }
  .contact { color: var(--grey-text); font-size: 11.5px; line-height: 1.5; }
  .contact-name {
    color: var(--navy); font-weight: 700; font-size: 16px;
    text-transform: uppercase; line-height: 1.2;
  }
  .contact-role { margin-bottom: 6px; }
  .contact-line { display: flex; align-items: center; gap: 6px; }
  .contact-line svg { width: 10px; height: 10px; flex: none; fill: var(--navy); }
  .address { margin-bottom: 4px; }

  .card-back { background: var(--navy-deep); }
  .back-pattern {
    position: absolute; inset: 0;
    background:
      radial-gradient(ellipse at 20% 25%, var(--navy-light) 0%, transparent 55%),
      radial-gradient(ellipse at 80% 80%, var(--navy-light) 0%, transparent 50%),
      linear-gradient(135deg, var(--navy-deep) 0%, var(--navy-dark) 100%);
  }
  .back-brand {
    position: absolute; right: 70px; top: 50%; transform: translateY(-50%);
    display: flex; align-items: center; gap: 10px;
  }
  .back-brand .brand-dot { background: #ffffff; width: 40px; height: 40px; }
  .back-brand .brand-name { color: #ffffff; font-size: 16px; }
</style>
</head>
<body>
<main class="stage">
  <section class="card card-front" aria-label="Business card front">
    <div class="brand">
      <span class="brand-dot"></span>
      <span class="brand-name">Wombat<br>Devices</span>
    </div>
    <div class="divider"></div>
    <div class="contact">
      <p class="contact-name">Dr Colin Marsh</p>
      <p class="contact-role">R&amp;D Engineer</p>
      <p class="address">PO Box XXX (to be confirmed)<br>Banks ACT 2913, Australia</p>
      <p class="contact-line">
        <svg viewBox="0 0 10 10"><path d="M2 0.5 3.8 2.6 2.8 3.8Q4 6 6.2 7.2L7.4 6.2 9.5 8 8.2 9.5Q3.5 8.5 0.5 1.8Z"/></svg>
        0427 563 210
      </p>
      <p class="contact-line">
        <svg viewBox="0 0 10 10"><path d="M0.5 2h9v6h-9zM1 2.5 5 5.5 9 2.5" stroke="#fff" stroke-width="0.8"/></svg>
        colin@wombatdevicesco.com.au
      </p>
      <p class="contact-line">
        <svg viewBox="0 0 10 10"><circle cx="5" cy="5" r="4.5"/><path d="M0.5 5h9M5 0.5v9M1.5 2.8h7M1.5 7.2h7" stroke="#fff" stroke-width="0.6"/></svg>
        www.wombatdevicesco.com.au
      </p>
    </div>
  </section>

  <section class="card card-back" aria-label="Business card back">
    <div class="back-pattern" role="img" aria-label="Faint tone-on-tone repeating brand emblem pattern across the navy card"></div>
    <div class="back-brand">
      <span class="brand-dot"></span>
      <span class="brand-name">Wombat Devices</span>
    </div>
  </section>
</main>
</body>
</html>
```